依頼概要
第33回白鷺川大星火大会
2018年7月14日(土)午後7時30分開会
関東最大級22800発
三大花火師夢の饗宴 桐原煙火工業・宮田火工製作所・藤屋松井火工店
主催:北浜町観光協会・きたはまみなと祭り実行委員会
後援:北浜町・北浜町議会・七森町・北浜町商工会・七森町商工会・JA北陸あおば
問い合わせ:北浜町観光協会 TEL0280-81-1319
北浜町で検索的なもの
観覧チケットの購入はチケミナで検索的なもの

若干の構成を再度お願いする場合もあります。また、制作いただきました作品に、場合によりこちらで後援や開催日時等軽微な修正をする場合があります。
http://filevault-sample.jp/photo/3c1a9e07b42d58f6a0e9c2147bd86f03e5a1c9d2
上記URLは添付にあるものと同様の使用する写真です

町長様・観光協会様の方で候補作品から選んでいただきました。

ご参加・ご協力ありがとうございました。

```html
<!DOCTYPE html>
<html lang="ja">
<head>
<meta charset="utf-8">
<title>第33回白鷺川大星火大会</title>
<link rel="stylesheet" href="https://fonts.googleapis.com/css2?family=Dela+Gothic+One&family=Zen+Maru+Gothic:wght@700;900&family=Noto+Sans+JP:wght@500;700;900&display=swap">
<style>
:root{
  --night:#050302;
  --gold:#ffd43a;
  --gold-deep:#e08a00;
  --ember:#b3240c;
  --red:#d9151b;
  --purple:#5a1f8c;
  --purple-deep:#3a0f63;
  --lavender:#e9dcf5;
  --paper:#fffdf6;
  --ink:#2a1a10;
}
*{margin:0;padding:0;box-sizing:border-box}
html,body{width:849px;height:1200px;overflow:hidden;background:var(--paper)}
.poster{position:relative;width:849px;height:1200px;overflow:hidden;font-family:"Noto Sans JP",sans-serif;color:var(--ink)}
.sky{position:absolute;left:0;top:0;width:849px;height:880px;
  background:
    radial-gradient(circle at 200px 200px,rgba(255,214,80,.75) 0,rgba(255,170,20,.35) 120px,transparent 260px),
    radial-gradient(circle at 560px 180px,rgba(255,210,70,.8) 0,rgba(240,150,10,.35) 140px,transparent 300px),
    radial-gradient(circle at 120px 560px,rgba(255,200,60,.6) 0,transparent 240px),
    radial-gradient(circle at 700px 560px,rgba(255,210,80,.6) 0,transparent 250px),
    linear-gradient(180deg,var(--night) 0,#1a0d02 70%,var(--paper) 100%);}
.edition{position:absolute;left:58px;top:168px;width:122px;height:122px;border-radius:50%;
  background:radial-gradient(circle,#fff6c4 0,var(--gold) 60%,var(--gold-deep) 100%);
  border:4px solid var(--ember);display:flex;flex-direction:column;align-items:center;justify-content:center;
  font-family:"Noto Sans JP",sans-serif;font-weight:900;color:var(--ember);line-height:1}
.edition .num{font-size:46px}
.edition .pre,.edition .post{font-size:24px}
.title{position:absolute;font-family:"Noto Sans JP",sans-serif;font-weight:900;color:var(--gold);
  -webkit-text-stroke:3px var(--ember);paint-order:stroke fill;
  text-shadow:5px 5px 0 #000;line-height:1;white-space:nowrap}
.title-river{left:186px;top:112px;font-size:172px;letter-spacing:-2px}
.title-event{left:124px;top:312px;font-size:136px;letter-spacing:-1px}
.scale{position:absolute;right:92px;top:466px;font-family:"Zen Maru Gothic",sans-serif;font-weight:900;
  font-size:38px;color:#fff;-webkit-text-stroke:4px var(--red);paint-order:stroke fill}
.shots{position:absolute;right:58px;top:512px;font-family:"Dela Gothic One",sans-serif;font-size:72px;line-height:1.1;
  color:var(--gold);-webkit-text-stroke:4px var(--red);paint-order:stroke fill;text-shadow:4px 4px 0 #000}
.banner{position:absolute;left:0;top:640px;width:849px;height:82px;
  background:linear-gradient(90deg,transparent,var(--lavender) 12%,#fff 50%,var(--lavender) 88%,transparent);
  display:flex;align-items:center;justify-content:center;
  font-family:"Zen Maru Gothic",sans-serif;font-weight:900;font-size:58px;color:var(--purple);letter-spacing:2px}
.makers{position:absolute;left:0;top:728px;width:849px;text-align:center;font-weight:900;font-size:32px;
  color:#fff;-webkit-text-stroke:4px var(--purple-deep);paint-order:stroke fill}
.date{position:absolute;left:0;top:892px;width:849px;text-align:center;font-weight:900;color:var(--purple);line-height:1;white-space:nowrap}
.date .big{font-size:68px}
.date .mid{font-size:42px}
.date .sm{font-size:30px}
.credits{position:absolute;left:40px;top:985px;width:560px;font-size:14px;line-height:1.8;font-weight:500}
.contact{position:absolute;right:40px;top:985px;text-align:right;font-size:14px;line-height:1.6;font-weight:700}
.contact .tel{font-size:26px;font-weight:900;color:var(--ink)}
.rule{position:absolute;left:40px;right:40px;top:1090px;height:2px;background:var(--gold-deep)}
.search{position:absolute;left:40px;top:1112px;width:770px;display:flex;justify-content:space-between;
  font-size:14px;font-weight:700;align-items:center}
.search b{font-size:20px;color:var(--red)}
.search .btn{display:inline-block;background:var(--red);color:#fff;padding:2px 8px;border-radius:3px;margin-left:6px;font-size:13px}
</style>
</head>
<body>
<main class="poster">
  <div class="sky" role="img" aria-label="夜空に広がる金色の花火の写真"></div>

  <div class="edition"><span class="pre">第</span><span class="num">33</span><span class="post">回</span></div>
  <h1>
    <span class="title title-river">白鷺川</span>
    <span class="title title-event">大星火大会</span>
  </h1>
  <div class="scale">関東最大級</div>
  <div class="shots">22800発!!</div>

  <div class="banner">三大花火師夢の饗宴</div>
  <div class="makers">桐原煙火工業・宮田火工製作所・藤屋松井火工店</div>

  <div class="date"><span class="big">2018</span><span class="mid">年</span><span class="big">7</span><span class="mid">月</span><span class="big">14</span><span class="mid">日</span><span class="sm">(土)</span> <span class="sm">午後7時30分</span> <span class="mid">開会</span></div>

  <div class="credits">
    <p>主催｜北浜町観光協会・きたはまみなと祭り実行委員会</p>
    <p>後援｜北浜町・北浜町議会・七森町・北浜町商工会・七森町商工会・JA北陸あおば</p>
  </div>
  <div class="contact">
    <p>問い合わせ｜北浜町観光協会</p>
    <p class="tel">TEL 0290-64-7725</p>
  </div>

  <div class="rule"></div>
  <div class="search">
    <p>白鷺川大星火大会については、<b>「北浜町」</b>で<span class="btn">検索</span></p>
    <p>観覧チケットのご購入は、<b>「チケミナ」</b>で<span class="btn">検索</span></p>
  </div>
</main>
</body>
</html>
```